New Business Card for Web Design/Internet Marketing Company

Looking for a great looking new business card. We are a 10 year old web design, internet marketing and website management company that works mostly with small businesses.

Our new card needs to better match the colors and style of our website, be bold, extremely usable and slightly edgy.

Target Market(s)

Small/Medium businesses that have websites

Industry/Entity Type

Internet

Requirements
Must have
• Front and back design, full color, rounded corners please

Must use the colors/style of our website (JPG provided)

INFO FOR CARDS (as readable as possible please)
Mark Pellow
President/CEO
mark@brightlanesites.com
Phone: 520-481-7093
Toll Free: 866-481-7093
Address: 4315 E. Kestrel Ave. Ste. 140, Tucson, AZ 85733

THINGS I WANT TO PROMOTE (if there is room):
1. Our Website - www.brightlanesites.com

2. Social Media
Twitter: @brightlanesites
Facebook: www.facebook.com/brightlanesites

3. Our Services
Web Design
Internet Marketing
Website Management

```html
<!DOCTYPE html>
<html lang="en">
<head>
<meta charset="utf-8">
<title>Brightlane Sites – Business Card</title>
<link href="https://fonts.googleapis.com/css2?family=Source+Sans+3:wght@400;600;700&display=swap" rel="stylesheet">
<style>
  :root {
    --bg: #e8e5e1;
    --card: #ffffff;
    --blue: #1a8fc6;
    --orange: #f28a3a;
    --orange-faint: #f9cba8;
    --text: #555b60;
    --text-dark: #3f4448;
  }
  * { box-sizing: border-box; margin: 0; padding: 0; }
  html, body { width: 1200px; height: 402px; overflow: hidden; }
  body {
    background: var(--bg);
    font-family: "Source Sans 3", sans-serif;
    color: var(--text);
    position: relative;
  }
  .card {
    position: absolute;
    top: 57px;
    width: 512px;
    height: 291px;
    background: var(--card);
    border-radius: 6px;
    box-shadow: 0 1px 3px rgba(0,0,0,.12);
    overflow: hidden;
  }
  .card--front { left: 68px; }
  .card--back { left: 622px; }

  /* front */
  .brand-name {
    position: absolute;
    left: 38px;
    top: 96px;
    font-size: 31px;
    font-weight: 700;
    color: var(--blue);
    line-height: 1;
    white-space: nowrap;
  }
  .brand-dot {
    display: inline-block;
    width: 12px; height: 12px;
    border-radius: 50%;
    background: var(--orange);
    margin-right: 8px;
    vertical-align: 4px;
  }
  .rule-front {
    position: absolute;
    left: 282px; right: 0;
    top: 118px;
    height: 2px;
    background: var(--blue);
  }
  .holder {
    position: absolute;
    right: 34px;
    top: 64px;
    text-align: right;
  }
  .holder__name { font-size: 19px; font-weight: 600; color: var(--blue); line-height: 1.1; }
  .holder__title { font-size: 12.5px; color: var(--text); margin-top: 2px; }
  .contact {
    position: absolute;
    right: 246px;
    top: 173px;
    list-style: none;
    text-align: right;
    font-size: 13px;
    line-height: 18.5px;
  }
  .contact li { display: flex; justify-content: flex-end; align-items: center; gap: 5px; }
  .contact svg { width: 10px; height: 10px; flex: none; }
  .address {
    position: absolute;
    right: 261px;
    top: 252px;
    text-align: right;
    font-size: 13px;
    line-height: 15px;
    font-style: normal;
  }
  .brand-faint {
    position: absolute;
    right: 22px;
    top: 200px;
    font-size: 40px;
    font-weight: 700;
    color: var(--orange-faint);
    line-height: 1;
    white-space: nowrap;
  }

  /* back */
  .brand-hero {
    position: absolute;
    left: 38px;
    top: 50px;
    font-size: 46px;
    font-weight: 700;
    color: var(--orange);
    line-height: 1;
  }
  .social {
    position: absolute;
    right: 35px;
    top: 124px;
    list-style: none;
    font-size: 13px;
    line-height: 18px;
  }
  .social li { display: flex; align-items: center; justify-content: flex-end; gap: 5px; }
  .social__mark { width: 11px; height: 11px; border-radius: 2px; background: var(--blue); }
  .services-rule {
    position: absolute;
    left: 0; right: 0;
    top: 196px;
    height: 2px;
    background: var(--blue);
  }
  .services-title {
    position: absolute;
    right: 18px;
    top: 181px;
    padding: 0 10px;
    background: var(--card);
    font-size: 20px;
    font-weight: 600;
    color: var(--blue);
    line-height: 1.3;
  }
  .services {
    position: absolute;
    right: 40px;
    top: 218px;
    list-style: none;
    text-align: right;
    font-size: 17.5px;
    line-height: 23px;
    color: var(--text-dark);
  }
</style>
</head>
<body>
  <section class="card card--front" aria-label="Card front">
    <div class="brand-name"><span class="brand-dot"></span>Brightlane Sites</div>
    <div class="rule-front"></div>
    <div class="holder">
      <p class="holder__name">Mark Pellow</p>
      <p class="holder__title">President/CEO</p>
    </div>
    <ul class="contact">
      <li>520-481-7093
        <svg viewBox="0 0 10 10" aria-hidden="true"><circle cx="5" cy="5" r="5" fill="#1a8fc6"/><path d="M3 2.5l1 1-.6.8c.4.9 1 1.5 1.9 1.9l.8-.6 1 1-.7.9C4.6 7.3 2.7 5.4 2.5 3.2z" fill="#fff"/></svg></li>
      <li>866-481-7093
        <svg viewBox="0 0 10 10" aria-hidden="true"><circle cx="5" cy="5" r="5" fill="#1a8fc6"/><path d="M3 2.5l1 1-.6.8c.4.9 1 1.5 1.9 1.9l.8-.6 1 1-.7.9C4.6 7.3 2.7 5.4 2.5 3.2z" fill="#fff"/></svg></li>
      <li>mark@brightlanesites.com
        <svg viewBox="0 0 10 10" aria-hidden="true"><rect x="0.5" y="2" width="9" height="6" rx="1" fill="#1a8fc6"/><path d="M1 2.5l4 3 4-3" stroke="#fff" stroke-width=".8" fill="none"/></svg></li>
      <li>www.brightlanesites.com
        <svg viewBox="0 0 10 10" aria-hidden="true"><circle cx="5" cy="5" r="4.4" fill="none" stroke="#1a8fc6" stroke-width="1.2"/><ellipse cx="5" cy="5" rx="1.8" ry="4.4" fill="none" stroke="#1a8fc6" stroke-width=".8"/><path d="M.8 5h8.4" stroke="#1a8fc6" stroke-width=".8"/></svg></li>
    </ul>
    <address class="address">4315 E. Kestrel Ave., Ste. 140<br>Tucson, AZ 85733</address>
    <div class="brand-faint" aria-hidden="true">Brightlane</div>
  </section>

  <section class="card card--back" aria-label="Card back">
    <div class="brand-hero">Brightlane<br>Sites</div>
    <ul class="social">
      <li><span class="social__mark"></span>@brightlanesites</li>
      <li><span class="social__mark"></span>brightlanesites</li>
    </ul>
    <div class="services-rule"></div>
    <h2 class="services-title">Our Services</h2>
    <ul class="services">
      <li>Web Design</li>
      <li>Internet Marketing</li>
      <li>Website Management</li>
    </ul>
  </section>
</body>
</html>
```